Business Card Design

Stronger Care Network for the Riverlands is a partnership of twenty different health organisations in the western suburbs of Melbourne, working together to improve the health of the local community. The western suburbs of Melbourne is one of the fastest growing and most culturally diverse populations in Australia and its communities have some of the poorest health outcomes in Australia.
Please see location for copy of the SCNR:
http://qvlr.com.au/fileadmin/filemount/pdf_files/SCNFTR_13_FINAL_JUNE_2012.pdf
Updates

Reason: Hello. I've extended the deadline because in the brief I made a confusing mention about a logo, but I actually meant the 'Stronger Care Network for the Riverlands' jpg that I had already attached. Sorry about the confusion Thanks Rosalind

Hello, Thanks for the designs I have already received. I have extended the deadline because I made a confusing reference to a logo in my brief, but I was talking about the 'Stronger Care Network for the Riverlands' jpg I had already attached. There is no other logo for me to provide.

Thanks, Rosalind

Target Market(s)

Health and state/local government managers and CEOs

Industry/Entity Type

Health

Contact Information for Business Card

Rosalind Tiernan
Executive Officer
Stronger Care Network for the Riverlands
Ph: 0438 295 614
Rosalind.Tiernan@kp.org.au

Requirements
Must have
• logo and details as provided.
Would prefer matt finish
I can't see that logo has successfully attached so if it has not, please email or call me to follow up.

```html
<!DOCTYPE html>
<html lang="en">
<head>
<meta charset="utf-8">
<title>Stronger Care Network for the Riverlands — Business Card</title>
<link rel="stylesheet" href="https://fonts.googleapis.com/css2?family=Arimo:wght@400&family=Roboto+Slab:wght@400&display=swap">
<style>
  :root {
    --backdrop: #d8d2c5;
    --card-white: #ffffff;
    --brand-blue: #1a86c8;
    --band-blue: #1d7cc2;
    --panel-blue: #1b98d5;
    --lime: #b6d86a;
    --navy: #1c2947;
    --shadow: rgba(60, 50, 30, 0.25);
  }
  * { box-sizing: border-box; margin: 0; padding: 0; }
  html, body {
    width: 1200px;
    height: 873px;
    overflow: hidden;
    background: var(--backdrop);
  }
  .canvas {
    width: 1200px;
    height: 873px;
    display: flex;
    align-items: center;
    justify-content: center;
    gap: 60px;
  }
  .card {
    position: relative;
    width: 510px;
    height: 310px;
    box-shadow: 0 6px 18px var(--shadow);
    overflow: hidden;
  }

  /* Front: contact details */
  .card--front {
    background: var(--card-white);
    font-family: "Arimo", Arial, sans-serif;
  }
  .contact {
    position: absolute;
    left: 40px;
    top: 34px;
    width: 320px;
  }
  .contact__name {
    color: var(--brand-blue);
    font-size: 25px;
    font-weight: 400;
    line-height: 1.2;
  }
  .contact__role {
    color: var(--navy);
    font-size: 18px;
    margin-top: 4px;
  }
  .contact__rule {
    display: block;
    margin: 30px 0 14px;
  }
  .contact__line {
    color: var(--brand-blue);
    font-size: 12.5px;
    line-height: 1.45;
  }
  .brand-band {
    position: absolute;
    left: 0;
    right: 0;
    bottom: 0;
    height: 58px;
    background: var(--band-blue);
    display: flex;
    align-items: center;
    padding-left: 40px;
  }
  .brand-band__name {
    color: var(--card-white);
    font-family: "Roboto Slab", Georgia, serif;
    font-weight: 400;
    font-size: 13px;
    letter-spacing: 0.6px;
    text-transform: uppercase;
    white-space: nowrap;
  }

  /* Back: organisation name panel */
  .card--back {
    background: var(--lime);
    padding: 14px;
  }
  .name-panel {
    width: 100%;
    height: 100%;
    background: var(--panel-blue);
    padding: 24px 30px;
  }
  .name-panel__title {
    width: 230px;
    color: var(--card-white);
    font-family: "Arimo", Arial, sans-serif;
    font-weight: 400;
    font-size: 30px;
    line-height: 1.08;
  }
</style>
</head>
<body>
  <main class="canvas">
    <section class="card card--front" aria-label="Business card front">
      <div class="contact">
        <h1 class="contact__name">Rosalind Tiernan</h1>
        <p class="contact__role">Executive Officer</p>
        <svg class="contact__rule" width="168" height="2" aria-hidden="true">
          <line x1="0" y1="1" x2="168" y2="1" stroke="var(--brand-blue)" stroke-width="2"/>
        </svg>
        <p class="contact__line">Ph: 0438 295 614</p>
        <p class="contact__line">rosalind.tiernan@kp.org.au</p>
      </div>
      <div class="brand-band">
        <p class="brand-band__name">Stronger Care Network for the Riverlands</p>
      </div>
    </section>

    <section class="card card--back" aria-label="Business card back">
      <div class="name-panel">
        <p class="name-panel__title">Stronger Care Network for the Riverlands</p>
      </div>
    </section>
  </main>
</body>
</html>
```